Creative, Innovative PowerPoint Sales Deck Refresh needed

We are a technology firm in the Dallas, TX area and we need the powerpoint presentation used for our sales calls refreshed. This presentation is used in one of the first meetings we have with potential clients, so we want to make a memorable and positive impact - we want something that sets us apart from everyone else. We need 8 master slide templates created for our sales deck and a series of slides within the example sales deck need to be completely refreshed (slides 31-37 and 43 in the sample ppt file) We want a sales deck that is modern, innovative, creative, memorable and whimsical - NOT a typical boring "business" design. Colors should match or compliment the colors used in our logo. The logo in the footer of the attached sample ppt is old - it should be replaced with the newer logo attached. Please take a look at our website to get an idea of our culture and aesthetic www.quorbinlab.com
Updates

Project Deadline Extended
Reason: We have received several designs we like and we want our entire team to have time to give them full consideration before making a decision.

Target Market(s)

Business executives

Industry/Entity Type

Information Technology

Font styles to use
Sans Serif

Requirements
Must have
• Our logo and LedgerWave logo in footer
• Master Slide Templates
• Rework / redesign of slides 31-37 and 43
Nice to have
• We use Raleway font in a lot of our materials

```html
<!DOCTYPE html>
<html lang="en">
<head>
<meta charset="utf-8">
<title>Sales Deck Slide Set</title>
<link href="https://fonts.googleapis.com/css2?family=Raleway:wght@400;500;600;700;800&display=swap" rel="stylesheet">
<style>
:root{
  --blue:#0f4f8c;
  --blue-dark:#0b3f70;
  --orange:#f27121;
  --green:#6cbf3f;
  --ink:#222;
  --grey:#8a8a8a;
  --light:#f2f4f6;
  --white:#fff;
}
*{box-sizing:border-box;margin:0;padding:0}
html,body{width:1200px;height:1164px;overflow:hidden;background:#fff}
body{font-family:'Raleway',sans-serif;color:var(--ink);position:relative}
.slide{position:absolute;width:398px;height:224px;background:#fff;overflow:hidden;box-shadow:0 1px 3px rgba(0,0,0,.25)}
.abs{position:absolute}
.title{position:absolute;left:20px;top:18px;font-size:18px;font-weight:400;letter-spacing:-.3px;color:var(--ink)}
.title::after{content:"";position:absolute;left:0;bottom:-6px;width:26px;height:2px;background:var(--blue)}
.rule{position:absolute;left:0;right:0;top:44px;height:1px;background:#e3e3e3}
.footer{position:absolute;left:0;right:0;bottom:0;height:20px;font-size:4px;color:var(--grey)}
.footer .brand{position:absolute;left:10px;top:5px;display:flex;align-items:center;gap:3px;font-size:5px;color:var(--ink);font-weight:600}
.footer .brand i{display:block;width:10px;height:10px;border-radius:50%;border:1.5px solid var(--blue)}
.footer .copy{position:absolute;left:78px;top:9px}
.footer .page{position:absolute;left:322px;top:9px;color:var(--ink)}
.footer .partner{position:absolute;right:10px;top:5px;display:flex;align-items:center;gap:3px;font-size:8px;font-weight:700;color:var(--ink)}
.footer .partner i{display:block;width:8px;height:8px;background:var(--blue)}
.photo{position:absolute}
.lorem{font-size:5px;line-height:1.35}
.white{color:#fff}
/* columns slide */
.col{position:absolute;top:0;width:80px;height:224px;padding:0 8px;color:#fff}
.col .icon{position:absolute;left:25px;top:50px;width:30px;height:30px;border:2px solid #fff;border-radius:50%}
.col h3{position:absolute;top:120px;left:8px;font-size:10px;font-weight:400;white-space:nowrap}
.col p{position:absolute;top:134px;left:8px;right:8px;font-size:5px;line-height:1.3;text-align:justify}
.tag{position:absolute;width:44px;height:14px;font-size:4.5px;color:#fff;padding:2px 4px;line-height:1.1}
.box{position:absolute;color:#fff;padding:6px}
.box h4{font-size:9px;font-weight:400;margin-bottom:3px}
.box p{font-size:4.5px;line-height:1.3}
.tile{position:absolute;width:76px;height:72px;color:#fff;text-align:center;padding:10px 6px 0}
.tile b{display:block;font-size:6px;margin-bottom:2px}
.tile span{font-size:5px;line-height:1.3;display:block}
.feat{position:absolute;font-size:5px;line-height:1.3;color:var(--grey)}
.feat b{display:block;font-size:6px;margin-bottom:2px}
</style>
</head>
<body>

<!-- Row 1 -->
<section class="slide" style="left:0;top:2px">
  <div class="col" style="left:0;background:var(--blue)"><div class="icon"></div><h3>Heading Here</h3><p>Lorem ipsum dolor sit amet, consectetur adipiscing elit, sed do eiusmod tempor incididunt ut labore et dolore magna aliqua. Ut enimad minim veniam, quis nostrud exercitation ullamco laboris</p></div>
  <div class="col" style="left:80px;background:var(--orange)"><div class="icon"></div><h3>Heading Here</h3><p>Lorem ipsum dolor sit amet, consectetur adipiscing elit, sed do eiusmod tempor incididunt ut labore et dolore magna aliqua. Ut enimad minim veniam, quis nostrud exercitation ullamco laboris</p></div>
  <div class="col" style="left:160px;background:var(--green)"><div class="icon"></div><h3>Heading Here</h3><p>Lorem ipsum dolor sit amet, consectetur adipiscing elit, sed do eiusmod tempor incididunt ut labore et dolore magna aliqua. Ut enimad minim veniam, quis nostrud exercitation ullamco laboris</p></div>
  <div class="col" style="left:240px;background:var(--blue)"><div class="icon"></div><h3>Heading Here</h3><p>Lorem ipsum dolor sit amet, consectetur adipiscing elit, sed do eiusmod tempor incididunt ut labore et dolore magna aliqua. Ut enimad minim veniam, quis nostrud exercitation ullamco laboris</p></div>
  <div class="col" style="left:320px;width:78px;background:var(--orange)"><div class="icon"></div><h3>Heading Here</h3><p>Lorem ipsum dolor sit amet, consectetur adipiscing elit, sed do eiusmod tempor incididunt ut labore et dolore magna aliqua. Ut enimad minim veniam, quis nostrud exercitation ullamco laboris</p></div>
</section>

<section class="slide" style="left:401px;top:2px">
  <div class="abs" style="left:20px;top:20px;font-size:16px">OUR MOCKUP AREA</div>
  <div class="abs" style="left:0;right:0;top:132px;bottom:0;background:var(--ink)"></div>
  <svg class="abs" style="left:0;top:0" width="398" height="224">
    <rect x="92" y="40" width="212" height="150" rx="4" fill="#222"/>
    <rect x="98" y="46" width="200" height="136" fill="#fff"/>
    <rect x="68" y="190" width="260" height="6" rx="2" fill="#ccc"/>
    <g stroke-width="1" fill="none">
      <line x1="60" y1="82" x2="140" y2="82" stroke="var(--blue)"/>
      <line x1="60" y1="114" x2="140" y2="114" stroke="var(--green)"/>
      <line x1="60" y1="156" x2="135" y2="156" stroke="var(--orange)"/>
      <line x1="262" y1="82" x2="340" y2="82" stroke="var(--orange)"/>
      <line x1="282" y1="114" x2="340" y2="114" stroke="var(--blue)"/>
      <line x1="258" y1="156" x2="340" y2="156" stroke="var(--green)"/>
    </g>
    <circle cx="140" cy="82" r="1.5" fill="var(--blue)"/><circle cx="140" cy="114" r="1.5" fill="var(--green)"/>
    <circle cx="262" cy="82" r="1.5" fill="var(--orange)"/><circle cx="258" cy="156" r="1.5" fill="var(--green)"/>
    <circle cx="140" cy="114" r="12" fill="none" stroke="var(--blue)" stroke-width="2"/>
    <line x1="166" y1="100" x2="166" y2="128" stroke="#333"/>
    <text x="172" y="117" font-family="Raleway,sans-serif" font-size="12" font-weight="600" fill="#333">quorbinlab</text>
  </svg>
  <div class="tag" style="left:20px;top:75px;background:var(--blue)">Your Text Goes Here</div>
  <div class="tag" style="left:20px;top:107px;background:var(--green)">Your Text Goes Here</div>
  <div class="tag" style="left:20px;top:149px;background:var(--orange)">Your Text Goes Here</div>
  <div class="tag" style="left:334px;top:75px;background:var(--orange)">Your Text Goes Here</div>
  <div class="tag" style="left:334px;top:107px;background:var(--blue)">Your Text Goes Here</div>
  <div class="tag" style="left:334px;top:149px;background:var(--green)">Your Text Goes Here</div>
</section>

<section class="slide" style="left:801px;top:2px">
  <div class="abs" style="left:0;top:0;width:199px;height:224px;background:var(--blue)"></div>
  <div class="abs" style="left:52px;top:36px;width:108px;height:108px;border:3px solid #fff;border-radius:50%;text-align:center;padding-top:30px;font-size:16px;line-height:1.25;color:#fff"><span style="color:var(--orange)">RIGHT</span><br>PICTURE<br>SLIDE</div>
  <div class="abs lorem white" style="left:70px;top:160px;width:80px;text-align:center;font-size:4.5px">Mauris quam dolor, cursus at porta et, luctus eget purus. Nunc tempor luctus interdum. Duis libero leo dignissim.</div>
  <svg class="abs" style="left:230px;top:40px" width="160" height="100">
    <g fill="var(--blue)"><rect x="10" y="20" width="7" height="70"/><rect x="58" y="40" width="7" height="50"/><rect x="106" y="30" width="7" height="60"/><rect x="150" y="20" width="7" height="70" opacity="0"/></g>
    <g fill="var(--orange)"><rect x="20" y="50" width="7" height="40"/><rect x="68" y="15" width="7" height="75"/><rect x="116" y="15" width="7" height="75"/></g>
    <g fill="var(--green)"><rect x="30" y="60" width="7" height="30"/><rect x="78" y="30" width="7" height="60"/><rect x="126" y="50" width="7" height="40"/><rect x="146" y="10" width="7" height="80"/></g>
    <text x="50" y="100" font-size="4" fill="#888" font-family="Raleway,sans-serif">■ Sales ■ Market ■ Cost</text>
  </svg>
  <svg class="abs" style="left:216px;top:148px" width="14" height="12"><polygon points="7,0 14,12 0,12" fill="var(--orange)"/></svg>
  <div class="abs" style="left:234px;top:140px;font-size:26px;font-weight:700;color:var(--blue)">85%</div>
  <div class="abs" style="left:234px;top:173px;font-size:6px;color:var(--orange);font-weight:600">Profit</div>
  <div class="abs lorem" style="left:234px;top:182px;width:78px;color:var(--grey);font-size:4.5px">Mauris quam dolor, cursus at porta et, luctus eget purus. Nunc tempor luctus interdum. Duis libero leo dignissim.</div>
</section>

<!-- Row 2 -->
<section class="slide" style="left:0;top:235px">
  <div class="abs" style="left:0;top:0;width:398px;height:130px;background:linear-gradient(120deg,var(--blue-dark),var(--blue) 60%,#3d7ab0)"></div>
  <div class="abs white" style="left:18px;top:14px;font-size:16px">OUR MOCKUP</div>
  <div class="abs" style="left:18px;top:38px;width:22px;height:2px;background:#fff"></div>
  <div class="abs white" style="left:18px;top:54px;font-size:10px">Heading Here</div>
  <div class="abs lorem white" style="left:18px;top:68px;width:150px">Lorem ipsum dolor sit amet, consectetur adipiscing elit, sed do eiusmod tempor incididunt ut labore et dolore magna aliqua. Ut enimad minim veniam, quis nostrud exercitation ullamco laboris</div>
  <svg class="abs" style="left:170px;top:18px" width="220" height="180">
    <rect x="0" y="0" width="220" height="150" rx="5" fill="#1e1e1e"/>
    <rect x="8" y="8" width="204" height="128" fill="#fff"/>
    <rect x="100" y="150" width="20" height="18" fill="#bbb"/>
    <rect x="80" y="166" width="60" height="6" rx="2" fill="#ddd"/>
    <circle cx="52" cy="76" r="11" fill="none" stroke="var(--blue)" stroke-width="2"/>
    <line x1="74" y1="60" x2="74" y2="92" stroke="#333"/>
    <text x="80" y="80" font-family="Raleway,sans-serif" font-size="13" font-weight="600" fill="#333">quorbinlab</text>
  </svg>
  <div class="abs" style="left:18px;top:149px;width:14px;height:14px;border-radius:50%;background:var(--blue)"></div>
  <div class="abs lorem" style="left:40px;top:150px;width:160px;color:var(--grey)">Lorem ipsum dolor sit amet, consectetur adipiscing elit, sed do eiusmod tempor incididunt ut labore et dolore magna aliqua. Ut enimad minim veniam quis nostrud</div>
  <div class="abs" style="left:18px;top:181px;width:14px;height:14px;border-radius:50%;background:var(--blue)"></div>
  <div class="abs lorem" style="left:40px;top:182px;width:160px;color:var(--grey)">Lorem ipsum dolor sit amet, consectetur adipiscing elit, sed do eiusmod tempor incididunt ut labore et dolore magna aliqua. Ut enimad minim veniam quis nostrud</div>
  <div class="footer"><div class="brand"><i></i>quorbinlab</div><div class="copy">© 2017 quorbinlab. All rights reserved</div><div class="page">22</div><div class="partner"><i></i>LedgerWave</div></div>
</section>

<section class="slide" style="left:401px;top:235px">
  <div class="abs" style="left:26px;top:44px;font-size:16px;line-height:1.25">THIS IS LINE<br>CHART SLIDE</div>
  <div class="abs" style="left:28px;top:99px;width:90px;height:14px;background:var(--blue);color:#fff;font-size:6px;text-align:center;line-height:14px">CREATIVE TEXT HERE</div>
  <div class="abs lorem" style="left:34px;top:130px;width:96px;color:var(--grey)"><span style="color:var(--blue)">Lorem Ipsum dolor</span> sit amet, consectetur adipiscing elit, sed do eiusmod tempor incididunt ut labore et commodo consequat dolore magna aliqua.</div>
  <svg class="abs" style="left:180px;top:30px" width="210" height="175" font-family="Raleway,sans-serif" font-size="4" fill="#888">
    <g text-anchor="end"><text x="10" y="8">5</text><text x="10" y="23">4.5</text><text x="10" y="38">4</text><text x="10" y="53">3.5</text><text x="10" y="68">3</text><text x="10" y="83">2.5</text><text x="10" y="98">2</text><text x="10" y="113">1.5</text><text x="10" y="128">1</text><text x="10" y="143">0.5</text><text x="10" y="158">0</text></g>
    <g text-anchor="middle"><text x="45" y="170">Category 1</text><text x="108" y="170">Category 2</text><text x="170" y="170">Category 3</text><text x="232" y="170" opacity="0">.</text></g>
    <text x="232" y="170" text-anchor="middle">Category 4</text>
    <polyline points="45,88 108,32 170,110 232,78" fill="none" stroke="var(--blue)" stroke-width="1.6"/>
    <polyline points="45,34 108,86 170,58 232,28" fill="none" stroke="var(--orange)" stroke-width="1.6"/>
    <g fill="var(--blue)"><circle cx="45" cy="88" r="1.8"/><circle cx="108" cy="32" r="1.8"/><circle cx="170" cy="110" r="1.8"/></g>
    <g fill="var(--orange)"><circle cx="45" cy="34" r="1.8"/><circle cx="108" cy="86" r="1.8"/><circle cx="170" cy="58" r="1.8"/></g>
  </svg>
  <div class="footer"><div class="brand"><i></i>quorbinlab</div><div class="copy">© 2017 quorbinlab. All rights reserved</div><div class="page">23</div><div class="partner"><i></i>LedgerWave</div></div>
</section>

<section class="slide" style="left:801px;top:235px">
  <div class="title">YOUR TITLE GOES HERE</div><div class="rule"></div>
  <div class="photo" role="img" aria-label="Photo of engineers at work" style="left:28px;top:58px;width:111px;height:66px;background:linear-gradient(135deg,#c9c9c9,#6e6e6e)"></div>
  <div class="box" style="left:142px;top:58px;width:111px;height:66px;background:var(--orange)"><h4>Heading Goes Here</h4><p>Lorem ipsum dolor sit amet, consectetur adipiscing elit, sed do eiusmod tempor incididunt ut labore et commodo consequat dolore magna aliqua.</p></div>
  <div class="photo" role="img" aria-label="Photo of machinery" style="left:256px;top:58px;width:111px;height:66px;background:linear-gradient(135deg,#aaa,#444)"></div>
  <div class="box" style="left:28px;top:127px;width:111px;height:66px;background:var(--blue)"><h4>Heading Goes Here</h4><p>Lorem ipsum dolor sit amet, consectetur adipiscing elit, sed do eiusmod tempor incididunt ut labore et commodo consequat dolore magna aliqua.</p></div>
  <div class="photo" role="img" aria-label="Photo of a team meeting" style="left:142px;top:127px;width:111px;height:66px;background:linear-gradient(135deg,#999,#2c2c2c)"></div>
  <div class="box" style="left:256px;top:127px;width:111px;height:66px;background:var(--green)"><h4>Heading Goes Here</h4><p>Lorem ipsum dolor sit amet, consectetur adipiscing elit, sed do eiusmod tempor incididunt ut labore et commodo consequat dolore magna aliqua.</p></div>
  <div class="footer"><div class="brand"><i></i>quorbinlab</div><div class="copy">© 2017 quorbinlab. All rights reserved</div><div class="page">24</div><div class="partner"><i></i>LedgerWave</div></div>
</section>

<!-- Row 3 -->
<section class="slide" style="left:0;top:468px">
  <div class="photo" role="img" aria-label="Photo of a business person touching a rising chart" style="left:0;top:0;width:278px;height:224px;background:linear-gradient(110deg,#dfe6ee,#b4c4d6 50%,#7c93ad)"></div>
  <div class="box" style="left:200px;top:48px;width:198px;height:126px;background:var(--blue);padding:14px 22px">
    <h4 style="font-size:16px;margin-bottom:8px">ABOUT US</h4>
    <p style="font-size:5.5px;margin-bottom:6px">Lorem ipsum dolor sit amet, consectetur adipiscing elit, sed do eiusmod tempor incididunt ut labore et dolore magna aliqua.</p>
    <p style="font-size:5.5px">Ut enimad minim veniam, quis nostrud exercitation ullamco laboris nisi ut aliquip ex ea commodo consequat.</p>
  </div>
  <div class="footer"><div class="page">25</div><div class="partner"><i></i>LedgerWave</div></div>
</section>

<section class="slide" style="left:401px;top:468px">
  <div class="photo" role="img" aria-label="Photo of a desk with headphones, tinted green" style="left:0;top:0;width:398px;height:224px;background:linear-gradient(160deg,#7fc15a,#5aa83a)"></div>
  <svg class="abs" style="left:0;top:0" width="398" height="224"><polygon points="398,120 398,224 270,224" fill="#fff"/><polygon points="398,100 398,124 250,224 230,224" fill="var(--green)" opacity=".9"/></svg>
  <div class="abs white" style="left:48px;top:92px;font-size:20px;font-weight:800;letter-spacing:-.2px">THIS IS YOUR DIVIDER PAGE</div>
  <div class="abs white" style="left:260px;top:120px;font-size:7px">Your Subtitle Goes Here</div>
  <div class="abs" style="left:326px;top:197px;display:flex;align-items:center;gap:3px;font-size:5px;font-weight:600"><i style="display:block;width:10px;height:10px;border-radius:50%;border:1.5px solid var(--blue)"></i>quorbinlab</div>
</section>

<section class="slide" style="left:801px;top:468px">
  <div class="title">QUOTE AREA</div>
  <div class="abs" style="left:0;top:60px;width:199px;height:138px;background:var(--blue)"></div>
  <div class="photo" role="img" aria-label="Photo of climbers helping each other up a rock at dusk" style="left:199px;top:60px;width:199px;height:138px;background:linear-gradient(180deg,#8fa3b5,#33404d)"></div>
  <div class="abs white" style="left:24px;top:108px;font-size:10px;line-height:1.35;width:200px">“ Coming together is a beginning.<br>Keeping together is progress.<br>Working together is success.<br><br>&nbsp;- Harold Penn -</div>
  <div class="footer"><div class="brand"><i></i>quorbinlab</div><div class="copy">© 2017 quorbinlab. All rights reserved</div><div class="page">27</div><div class="partner"><i></i>LedgerWave</div></div>
</section>

<!-- Row 4 -->
<section class="slide" style="left:0;top:700px">
  <div class="title">BRAND DETAILED</div><div class="rule"></div>
  <div class="photo" role="img" aria-label="Photo of a man reading in a warehouse" style="left:27px;top:56px;width:170px;height:143px;background:linear-gradient(120deg,#d6d6d6,#6b6b6b)"></div>
  <div class="tile" style="left:213px;top:56px;background:var(--blue)"><b>System</b><span>Mauris quam dolor, cursus at porta et, luctus eget purus. Nunc tempor luctus interdum.</span></div>
  <div class="tile" style="left:293px;top:56px;background:var(--orange)"><b>Technology</b><span>Mauris quam dolor, cursus at porta et, luctus eget purus. Nunc tempor luctus interdum.</span></div>
  <div class="tile" style="left:213px;top:130px;background:var(--green)"><b>Leisure</b><span>Mauris quam dolor, cursus at porta et, luctus eget purus. Nunc tempor luctus interdum.</span></div>
  <div class="tile" style="left:293px;top:130px;background:var(--blue)"><b>Digital</b><span>Mauris quam dolor, cursus at porta et, luctus eget purus. Nunc tempor luctus interdum.</span></div>
  <div class="footer"><div class="brand"><i></i>quorbinlab</div><div class="copy">© 2017 quorbinlab. All rights reserved</div><div class="page">28</div><div class="partner"><i></i>LedgerWave</div></div>
</section>

<section class="slide" style="left:401px;top:700px">
  <div class="title">PRODUCT PHILOSOPHY</div><div class="rule"></div>
  <svg class="abs" style="left:0;top:0" width="398" height="224" font-family="Raleway,sans-serif">
    <g transform="rotate(-90 200 125)" fill="none" stroke-width="22">
      <circle cx="200" cy="125" r="40" stroke="var(--ink)" stroke-dasharray="87.96 251.3"/>
      <circle cx="200" cy="125" r="40" stroke="var(--green)" stroke-dasharray="0 87.96 50.27 251.3"/>
      <circle cx="200" cy="125" r="40" stroke="var(--orange)" stroke-dasharray="0 138.23 62.83 251.3"/>
      <circle cx="200" cy="125" r="40" stroke="var(--blue)" stroke-dasharray="0 201.06 50.27 251.3"/>
    </g>
    <circle cx="200" cy="125" r="29" fill="#fff"/>
    <text x="200" y="130" text-anchor="middle" font-size="13" font-weight="800" fill="#222">NOVA</text>
    <g font-size="7" font-weight="700" fill="#fff"><text x="178" y="100">20%</text><text x="224" y="110">35%</text><text x="213" y="158">40%</text><text x="166" y="152">30%</text></g>
    <circle cx="118" cy="78" r="18" fill="var(--blue)"/><circle cx="282" cy="78" r="18" fill="var(--ink)"/>
    <circle cx="118" cy="172" r="18" fill="var(--orange)"/><circle cx="282" cy="172" r="18" fill="var(--green)"/>
    <g fill="none" stroke="#fff" stroke-width="1.5"><circle cx="118" cy="78" r="8"/><circle cx="282" cy="78" r="8"/><circle cx="118" cy="172" r="8"/><rect x="274" y="165" width="16" height="14"/></g>
  </svg>
  <div class="feat" style="left:22px;top:62px;width:74px;text-align:right"><b style="color:var(--blue)">Secure</b>Nullam eu tempor purus. Nunc a leo magna, sit amet consequat risus.</div>
  <div class="feat" style="left:306px;top:62px;width:74px"><b style="color:var(--ink)">Well Organized</b>Nullam eu tempor purus. Nunc a leo magna, sit amet consequat risus.</div>
  <div class="feat" style="left:22px;top:156px;width:74px;text-align:right"><b style="color:var(--orange)">Good Package</b>Nullam eu tempor purus. Nunc a leo magna, sit amet consequat risus.</div>
  <div class="feat" style="left:306px;top:156px;width:74px"><b style="color:var(--green)">Publication</b>Nullam eu tempor purus. Nunc a leo magna, sit amet consequat risus.</div>
  <div class="footer"><div class="brand"><i></i>quorbinlab</div><div class="copy">© 2017 quorbinlab. All rights reserved</div><div class="page">29</div><div class="partner"><i></i>LedgerWave</div></div>
</section>

<section class="slide" style="left:801px;top:700px">
  <div class="photo" role="img" aria-label="Faded photo of a city skyline" style="left:0;top:0;width:398px;height:160px;background:linear-gradient(180deg,#fafafa,#dfe3e6)"></div>
  <div class="abs" style="left:0;top:158px;width:398px;height:66px;background:var(--blue)"></div>
  <svg class="abs" style="left:0;top:0" width="398" height="224" font-family="Raleway,sans-serif" font-size="8" text-anchor="middle">
    <text x="200" y="38" font-size="5" fill="#555" text-anchor="start"><tspan fill="var(--orange)">■</tspan> 2014 <tspan fill="var(--green)">■</tspan> 2015</text>
    <g fill="var(--orange)"><rect x="42" y="94" width="24" height="64"/><rect x="130" y="110" width="24" height="48"/><rect x="218" y="112" width="24" height="46"/><rect x="306" y="126" width="24" height="32"/></g>
    <g fill="var(--green)"><rect x="72" y="78" width="24" height="80"/><rect x="160" y="62" width="24" height="96"/><rect x="248" y="126" width="24" height="32"/><rect x="336" y="142" width="24" height="16"/></g>
    <g fill="var(--orange)"><text x="54" y="90">400</text><text x="142" y="106">300</text><text x="230" y="108">290</text><text x="318" y="122">200</text></g>
    <g fill="var(--green)"><text x="84" y="74">500</text><text x="172" y="58">600</text><text x="260" y="122">200</text><text x="348" y="138">100</text></g>
    <g fill="#fff" font-size="6" font-weight="600"><text x="60" y="172">Asia</text><text x="154" y="172">Africa</text><text x="244" y="172">America</text><text x="334" y="172">Euro</text></g>
    <g fill="#fff" font-size="4"><text x="60" y="180">Duis quis purus adipiscing mi</text><text x="60" y="185">scelerisque dictum quis vel eros.</text><text x="60" y="190">Nullam eu tempor purus.</text>
    <text x="154" y="180">Duis quis purus adipiscing mi</text><text x="154" y="185">scelerisque dictum quis vel eros.</text><text x="154" y="190">Nullam eu tempor purus.</text>
    <text x="244" y="180">Duis quis purus adipiscing mi</text><text x="244" y="185">scelerisque dictum quis vel eros.</text><text x="244" y="190">Nullam eu tempor purus.</text>
    <text x="334" y="180">Duis quis purus adipiscing mi</text><text x="334" y="185">scelerisque dictum quis vel eros.</text><text x="334" y="190">Nullam eu tempor purus.</text></g>
  </svg>
</section>

<!-- Row 5 -->
<section class="slide" style="left:0;top:933px">
  <div class="title">TRENDING IN THE WORLD</div><div class="rule"></div>
  <div class="photo" role="img" aria-label="Grey world map" style="left:20px;top:55px;width:250px;height:140px;background:radial-gradient(ellipse at center,#d4d4d4 40%,#fff 72%)"></div>
  <svg class="abs" style="left:0;top:0" width="398" height="224" font-family="Raleway,sans-serif" text-anchor="middle">
    <circle cx="47" cy="119" r="14" fill="var(--green)" opacity=".9"/><text x="47" y="123" font-size="10" fill="#fff">25%</text>
    <circle cx="125" cy="108" r="21" fill="var(--orange)" opacity=".9"/><text x="125" y="113" font-size="13" fill="#fff">80%</text>
    <circle cx="235" cy="114" r="22" fill="#3a3a3a" opacity=".95"/><text x="235" y="119" font-size="13" fill="#fff">75%</text>
    <circle cx="194" cy="152" r="13" fill="var(--orange)" opacity=".85"/><text x="194" y="156" font-size="9" fill="#fff">15%</text>
    <g fill="none" stroke-width="2"><circle cx="292" cy="78" r="12" stroke="var(--orange)"/><circle cx="292" cy="120" r="12" stroke="var(--ink)"/><circle cx="292" cy="162" r="12" stroke="var(--green)"/></g>
  </svg>
  <div class="feat" style="left:312px;top:67px;width:76px"><b style="color:var(--orange);font-weight:400">Confusion</b>Nullam eu tempor purus. Nunc a leo magna, sit amet consequat risus.</div>
  <div class="feat" style="left:312px;top:109px;width:76px"><b style="color:var(--ink);font-weight:400">Intangible</b>Nullam eu tempor purus. Nunc a leo magna, sit amet consequat risus.</div>
  <div class="feat" style="left:312px;top:151px;width:76px"><b style="color:var(--green);font-weight:400">Performance</b>Nullam eu tempor purus. Nunc a leo magna, sit amet consequat risus.</div>
  <div class="footer"><div class="brand"><i></i>quorbinlab</div><div class="copy">© 2017 quorbinlab. All rights reserved</div><div class="page">31</div><div class="partner"><i></i>LedgerWave</div></div>
</section>

<section class="slide" style="left:401px;top:933px">
  <div class="title">OUR VISION &amp; MISSION</div>
  <div class="photo" role="img" aria-label="Photo of a workspace tinted deep blue" style="left:0;top:52px;width:398px;height:148px;background:linear-gradient(160deg,#1a5a96,#0b3f70)"></div>
  <div class="abs white" style="left:20px;top:66px;font-size:11px">• Our Vision:</div>
  <div class="abs white" style="left:26px;top:82px;font-size:8.5px;font-weight:700;line-height:1.3">Go to the Next Level<br>Without look in the past</div>
  <div class="abs lorem white" style="left:26px;top:114px;width:165px">Lorem ipsum dolor sit amet, consectetur adipiscing elit, sed do eiusmod tempor incididunt ut labore et dolore magna aliqua. Ut enimad minim veniam, quis nostrud exercitation ullamco laboris nisi ut aliquip ex ea commodo consequat.</div>
  <div class="abs white" style="left:222px;top:66px;font-size:11px">• Our Missions:</div>
  <div class="abs" style="left:230px;top:85px;width:14px;height:14px;border-radius:50%;border:1.5px solid #fff"></div>
  <div class="abs white" style="left:256px;top:82px;font-size:10px">Your Text Here</div>
  <div class="abs lorem white" style="left:256px;top:95px;width:135px">Lorem ipsum dolor sit consectetur adipiscing elit, sed do eiusmod tempo.</div>
  <div class="abs" style="left:230px;top:116px;width:14px;height:14px;border-radius:50%;border:1.5px solid #fff"></div>
  <div class="abs white" style="left:256px;top:113px;font-size:10px">Your Text Here</div>
  <div class="abs lorem white" style="left:256px;top:126px;width:135px">Lorem ipsum dolor sit consectetur adipiscing elit, sed do eiusmod tempo.</div>
  <div class="abs" style="left:230px;top:148px;width:14px;height:14px;border-radius:50%;border:1.5px solid #fff"></div>
  <div class="abs white" style="left:256px;top:145px;font-size:10px">Your Text Here</div>
  <div class="abs lorem white" style="left:256px;top:158px;width:135px">Lorem ipsum dolor sit consectetur adipiscing elit, sed do eiusmod tempo.</div>
  <div class="footer"><div class="brand"><i></i>quorbinlab</div><div class="copy">© 2017 quorbinlab. All rights reserved</div><div class="page">32</div><div class="partner"><i></i>LedgerWave</div></div>
</section>

<section class="slide" style="left:801px;top:933px">
  <div class="title">OUR SERVICES</div><div class="rule"></div>
  <div class="photo" role="img" aria-label="Photo of chess pieces on a board" style="left:36px;top:52px;width:155px;height:98px;background:linear-gradient(135deg,#a88a6c,#3b2c20)"></div>
  <div class="abs" style="left:36px;top:160px;font-size:7px;color:var(--blue)">Your Title Goes Here</div>
  <div class="abs lorem" style="left:36px;top:170px;width:160px;color:var(--grey);font-size:4.5px">Lorem ipsum dolor sit amet, consectetur adipiscing elit, sed do eiusmod tempor incididunt ut labore et dolore magna aliqua. Ut enimad minim veniam, quis nostrud exercitation ullamco laboris nisi ut aliquip ex ea commodo consequat.</div>
  <div class="abs" style="left:216px;top:54px;width:16px;height:16px;border-radius:50%;background:var(--blue)"></div>
  <div class="feat" style="left:244px;top:54px;width:140px"><b style="color:var(--blue);font-weight:400;font-size:7px">Service Number One</b>Lorem ipsum dolor sit amet, consectetur adipiscing elit, sed do eiusmod tempor incididunt ut labore et dolore magna aliqua.</div>
  <div class="abs" style="left:216px;top:102px;width:16px;height:16px;border-radius:50%;background:var(--blue)"></div>
  <div class="feat" style="left:244px;top:102px;width:140px"><b style="color:var(--blue);font-weight:400;font-size:7px">Service Number Two</b>Lorem ipsum dolor sit amet, consectetur adipiscing elit, sed do eiusmod tempor incididunt ut labore et dolore magna aliqua.</div>
  <div class="abs" style="left:216px;top:150px;width:16px;height:16px;border-radius:50%;background:var(--blue)"></div>
  <div class="feat" style="left:244px;top:150px;width:140px"><b style="color:var(--blue);font-weight:400;font-size:7px">Service Number Three</b>Lorem ipsum dolor sit amet, consectetur adipiscing elit, sed do eiusmod tempor incididunt ut labore et dolore magna aliqua.</div>
  <div class="footer"><div class="brand"><i></i>quorbinlab</div><div class="copy">© 2017 quorbinlab. All rights reserved</div><div class="page">33</div><div class="partner"><i></i>LedgerWave</div></div>
</section>

</body>
</html>
```